Business cards for Harbourline Supply Pty Ltd that import building products into Australia from China
Target Market(s)
Business to Business
Industry/Entity Type
Business
Contact Information for Business Card
Front: Logo and Business Name
Rear:
Vernon Ashcombe
General Manager
Mobile: 0427 619 354
email: vern@harbourlinesupply.com.au
alternative email: vern@coastwardgoods.com.au
web: www.harbourlinesupply.com.au
Adelaide, Brisbane and Darwin
Colors
ec1f27
fbee3d

```html
<!DOCTYPE html>
<html lang="en">
<head>
<meta charset="utf-8">
<title>Harbourline Supply Pty Ltd — Business Cards</title>
<link rel="stylesheet" href="https://fonts.googleapis.com/css2?family=Open+Sans:wght@400;600;700&display=swap">
<style>
  :root {
    --brand-red: #ec1f27;
    --brand-yellow: #fbee3d;
    --ink: #231f20;
    --ink-soft: #3a3a3a;
    --paper: #f7f7f5;
    --backdrop: #3b3431;
  }
  * { box-sizing: border-box; margin: 0; padding: 0; }
  html, body {
    width: 1200px;
    height: 844px;
    overflow: hidden;
  }
  body {
    background: var(--backdrop);
    font-family: "Open Sans", Arial, sans-serif;
    position: relative;
  }
  .card {
    position: absolute;
    width: 500px;
    height: 300px;
    border-radius: 2px;
  }
  /* Contact side */
  .card--contact {
    left: 70px;
    top: 440px;
    background: var(--paper);
    color: var(--ink);
  }
  .brand-lockup {
    position: absolute;
    right: 34px;
    top: 40px;
    text-align: right;
  }
  .brand-lockup__name {
    display: flex;
    align-items: center;
    justify-content: flex-end;
    gap: 10px;
    font-weight: 700;
    font-size: 30px;
    line-height: 1;
    color: var(--ink);
    letter-spacing: -0.5px;
  }
  .brand-lockup__mark {
    width: 22px;
    height: 22px;
    background: var(--brand-red);
    flex: none;
  }
  .person {
    position: absolute;
    left: 34px;
    top: 150px;
  }
  .person__name {
    font-size: 17px;
    font-weight: 600;
    letter-spacing: 0.3px;
    color: var(--ink);
  }
  .person__surname { color: var(--brand-red); }
  .person__role {
    font-size: 12.5px;
    color: var(--ink-soft);
    margin-top: 1px;
  }
  .contact {
    position: absolute;
    left: 34px;
    top: 208px;
    font-size: 12.5px;
    color: var(--ink-soft);
    line-height: 1.75;
  }
  .contact__cities { margin-bottom: 6px; }
  .contact__label {
    color: var(--brand-red);
    font-weight: 700;
  }
  .contact__row span + span { margin-left: 10px; }
  .contact__web { color: var(--ink); font-weight: 600; }
  .contact__web-domain { color: var(--brand-red); }

  /* Brand side */
  .card--brand {
    left: 630px;
    top: 104px;
    background: var(--brand-red);
    display: flex;
    align-items: center;
    justify-content: center;
  }
  .card--brand .brand-lockup__name {
    color: #ffffff;
    font-size: 34px;
  }
  .card--brand .brand-lockup__mark { background: #ffffff; }
</style>
</head>
<body>

  <section class="card card--contact" aria-label="Business card, contact side">
    <div class="brand-lockup">
      <div class="brand-lockup__name">
        <span class="brand-lockup__mark" aria-hidden="true"></span>
        <span>Harbourline Supply</span>
      </div>
    </div>

    <div class="person">
      <p class="person__name">VERNON <span class="person__surname">ASHCOMBE</span></p>
      <p class="person__role">General Manager</p>
    </div>

    <div class="contact">
      <p class="contact__cities">Adelaide, Brisbane and Darwin</p>
      <p class="contact__row">
        <span><span class="contact__label">M:</span> 0427 619 354</span>
        <span><span class="contact__label">E:</span> vern@harbourlinesupply.com.au</span>
      </p>
      <p class="contact__row">
        <span><span class="contact__label">E:</span> vern@coastwardgoods.com.au</span>
        <span class="contact__web">www.<span class="contact__web-domain">harbourlinesupply</span>.com.au</span>
      </p>
    </div>
  </section>

  <section class="card card--brand" aria-label="Business card, brand side">
    <div class="brand-lockup__name">
      <span class="brand-lockup__mark" aria-hidden="true"></span>
      <span>Harbourline Supply</span>
    </div>
  </section>

</body>
</html>
```